Website for IT consulting Company

I need a website upgrade, the existing site content is ok, I would also like to add a testimonial page, the site should be something that is easy for us to update content. You use the content from www.velmarketa.com as an example. I will also post update logo and artwork. I also need a contact form with some type of validation or captcha.

Please omit Address maps

Target Market(s)

small business, service oriented companies. We provide IT Consulting, support and mangement

Industry/Entity Type

Information Technology

Coding

Coded - Design and coding required

Number of Pages Required

1 page

Font styles to use
Serif
Sans Serif

Requirements
Must have
• Contain logo attached, and content from existing web site www.velmarketa.com.
• Also need to update content easily, and be movable to different platforms.
• There is a catch phrase
• "Let us worry about your technology…” “ so you don’t have to!”
• Should be included.
Nice to have
• Testimonial page, Project page where we can post new and past projects and pictures
Should not have
• none

```html
<!DOCTYPE html>
<html lang="en">
<head>
<meta charset="utf-8">
<title>Velmarketa – IT Solutions</title>
<link href="https://fonts.googleapis.com/css2?family=Open+Sans:wght@400;600;700&family=Arimo:wght@400;700&display=swap" rel="stylesheet">
<style>
:root{
  --orange:#f07a2a;
  --orange-head:#f7931e;
  --dark:#1b1b1b;
  --darker:#141414;
  --light:#f2f2f2;
  --text:#444;
  --muted:#777;
  --white:#fff;
}
*{margin:0;padding:0;box-sizing:border-box}
html,body{width:1023px;height:1200px;overflow:hidden}
body{position:relative;background:var(--light);font-family:"Arimo",Arial,sans-serif;color:var(--text)}
.topbar{position:absolute;left:0;top:0;width:1023px;height:84px;background:var(--dark);border-bottom:1px solid #2a2a2a}
.topbar__title{position:absolute;left:56px;top:17px;font-family:"Open Sans",sans-serif;font-weight:700;font-size:25px;color:var(--orange-head);letter-spacing:-.2px}
.topbar__sub{position:absolute;left:56px;top:57px;font-size:11.5px;font-weight:700;color:var(--white);letter-spacing:-.2px}
.social{position:absolute;left:790px;top:25px;display:flex;gap:4px}
.social span{width:19px;height:19px;background:#3a3a3a;display:block}
.search{position:absolute;left:956px;top:29px}
.navbar{position:absolute;left:0;top:84px;width:1023px;height:97px;background:var(--darker)}
.brand{position:absolute;left:56px;top:27px;display:flex;align-items:center;gap:10px}
.brand__mark{width:44px;height:44px;background:var(--orange);display:block}
.brand__name{font-family:"Open Sans",sans-serif;font-weight:700;font-size:34px;color:#bfbfbf;letter-spacing:-1px;line-height:1}
.nav{position:absolute;top:36px;left:0;width:1023px;font-size:12px;color:var(--white);letter-spacing:-.3px}
.nav a{position:absolute;color:var(--white);text-decoration:none;line-height:27px}
.nav .is-active{background:var(--orange);padding:0 10px;border-radius:2px}
.hero{position:absolute;left:0;top:181px;width:1023px;height:400px;background:linear-gradient(115deg,#5a6878 0%,#c9ced6 35%,#e9ecf1 60%,#d8dde6 100%)}
.hero__title{position:absolute;left:56px;top:118px;font-family:"Open Sans",sans-serif;font-weight:600;font-size:29px;line-height:31px;color:var(--white);width:480px}
.hero__text{position:absolute;left:56px;top:198px;font-family:"Open Sans",sans-serif;font-weight:600;font-size:12.5px;color:var(--white)}
.hero__btn{position:absolute;left:56px;top:240px;width:87px;height:30px;background:var(--orange);color:var(--white);font-size:12px;line-height:30px;text-align:center;border-radius:2px}
.hero__arrow{position:absolute;top:180px;width:32px;height:32px;background:var(--orange);border-radius:2px;display:flex;align-items:center;justify-content:center}
.hero__dots{position:absolute;left:465px;top:354px;display:flex;gap:12px}
.hero__dots span{width:19px;height:19px;border-radius:50%;background:var(--white);border:2px solid #ddd}
.hero__dots .is-current{background:var(--orange);border-color:var(--orange)}
.services__title{position:absolute;left:0;top:632px;width:1023px;text-align:center;font-family:"Open Sans",sans-serif;font-weight:600;font-size:30px;color:#555}
.services__intro{position:absolute;left:240px;top:685px;width:543px;text-align:center;font-size:13px;line-height:19px;color:#444}
.service{position:absolute;width:300px;height:90px}
.service__icon{position:absolute;left:0;top:0;width:88px;height:88px;border-radius:50%;background:var(--white);box-shadow:0 0 0 3px #e8e8e8;display:flex;align-items:center;justify-content:center}
.service__name{position:absolute;left:108px;top:8px;font-family:"Open Sans",sans-serif;font-weight:600;font-size:13px;color:#444}
.service__text{position:absolute;left:108px;top:37px;font-family:"Open Sans",sans-serif;font-size:13.5px;line-height:19px;color:var(--muted)}
.about{position:absolute;left:0;top:1056px;width:1023px;height:144px;background:linear-gradient(90deg,#2b2b2b,#3a3836 50%,#2b2b2b)}
.about__title{position:absolute;left:0;top:52px;width:1023px;text-align:center;font-family:"Open Sans",sans-serif;font-weight:700;font-size:30px;color:var(--white)}
.about__text{position:absolute;left:56px;top:104px;width:911px;text-align:center;font-size:13px;line-height:19px;color:var(--white);letter-spacing:-.35px}
</style>
</head>
<body>
<header class="topbar">
  <div class="topbar__title">IT SOLUTIONS THAT WORK FOR YOUR BUSINESS</div>
  <div class="topbar__sub">A FULL SERVICE TECHNOLOGY COMPANY</div>
  <div class="social"><span></span><span></span><span></span><span></span><span></span></div>
  <svg class="search" width="11" height="11" viewBox="0 0 12 12"><circle cx="5" cy="5" r="3.6" fill="none" stroke="#fff" stroke-width="1.8"/><path d="M7.6 7.6 11 11" stroke="#fff" stroke-width="2"/></svg>
</header>
<div class="navbar">
  <div class="brand">
    <span class="brand__mark"></span>
    <span class="brand__name">VELMARKETA</span>
  </div>
  <nav class="nav">
    <a class="is-active" style="left:473px">Home</a>
    <a style="left:559px">About Us</a>
    <a style="left:652px">Support</a>
    <a style="left:739px">Clients</a>
    <a style="left:820px">Careers</a>
    <a style="left:907px">Contact</a>
  </nav>
</div>
<section class="hero" role="img" aria-label="Photo of business people reviewing charts and a tablet">
  <div class="hero__title">Lorem ipsum dolor sit amet consectetur adipisicing elit</div>
  <div class="hero__text">Accusantium doloremque laudantium totam rem aperiam, eaque ipsa...</div>
  <div class="hero__btn">Read More</div>
  <div class="hero__arrow" style="left:8px"><svg width="10" height="12" viewBox="0 0 10 12"><path d="M7 1 2 6l5 5" fill="none" stroke="#fff" stroke-width="2.2"/></svg></div>
  <div class="hero__arrow" style="left:983px"><svg width="10" height="12" viewBox="0 0 10 12"><path d="M3 1l5 5-5 5" fill="none" stroke="#fff" stroke-width="2.2"/></svg></div>
  <div class="hero__dots"><span class="is-current"></span><span></span><span></span></div>
</section>
<h2 class="services__title">IT Support Solutions</h2>
<p class="services__intro">Lorem ipsum dolor sit amet, consectetur adipisicing elit, sed do eiusmod tempor incididunt ut et dolore magna aliqua. Ut enim ad minim veniam</p>

<div class="service" style="left:58px;top:786px">
  <div class="service__icon"><svg width="40" height="36" viewBox="0 0 40 36" fill="#f07a2a"><path d="M4 12h8l20-9v28l-20-9H4z"/><path d="M8 22h7l3 11h-7z"/><rect x="34" y="13" width="4" height="8"/></svg></div>
  <div class="service__name">NETWORK ADMINISTRATION</div>
  <div class="service__text">Lorem ipsum dolor sit amet,<br>consectetur adipisicing elit</div>
</div>
<div class="service" style="left:370px;top:786px">
  <div class="service__icon"><svg width="40" height="34" viewBox="0 0 40 34" fill="#f07a2a"><ellipse cx="16" cy="12" rx="15" ry="10"/><path d="M6 19 3 27l10-5z"/><ellipse cx="26" cy="21" rx="12" ry="8" stroke="#fff" stroke-width="2"/><path d="M33 26l4 6-9-4z"/></svg></div>
  <div class="service__name">DESKTOP SUPPORT</div>
  <div class="service__text">Lorem ipsum dolor sit amet,<br>consectetur adipisicing elit</div>
</div>
<div class="service" style="left:682px;top:786px">
  <div class="service__icon"><svg width="42" height="32" viewBox="0 0 42 32"><path d="M10 31a9 9 0 0 1-1-18 12 12 0 0 1 23-2 10 10 0 0 1 1 20z" fill="#f07a2a"/><path d="M18 9h6v9h5l-8 8-8-8h5z" fill="#fff"/></svg></div>
  <div class="service__name">NETWORK CABLING</div>
  <div class="service__text">Lorem ipsum dolor sit amet,<br>consectetur adipisicing elit</div>
</div>
<div class="service" style="left:58px;top:907px">
  <div class="service__icon"><svg width="40" height="32" viewBox="0 0 40 32"><path d="M6 28C4 14 18 4 38 4 36 22 24 30 6 28z" fill="#f07a2a"/><path d="M3 31C12 20 22 14 32 10" stroke="#fff" stroke-width="2.5" fill="none"/></svg></div>
  <div class="service__name">WIRELESS NETWORKS</div>
  <div class="service__text">Lorem ipsum dolor sit amet,<br>consectetur adipisicing elit</div>
</div>
<div class="service" style="left:370px;top:907px">
  <div class="service__icon"><svg width="42" height="40" viewBox="0 0 42 40" fill="#f07a2a"><circle cx="15" cy="22" r="10"/><circle cx="15" cy="22" r="14" fill="none" stroke="#f07a2a" stroke-width="5" stroke-dasharray="5 4"/><circle cx="15" cy="22" r="4" fill="#fff"/><circle cx="33" cy="9" r="5"/><circle cx="33" cy="9" r="2" fill="#fff"/><circle cx="33" cy="31" r="5"/><circle cx="33" cy="31" r="2" fill="#fff"/></svg></div>
  <div class="service__name">ANTIVIRUS SOLUTIONS</div>
  <div class="service__text">Lorem ipsum dolor sit amet,<br>consectetur adipisicing elit</div>
</div>
<div class="service" style="left:682px;top:907px">
  <div class="service__icon"><svg width="40" height="34" viewBox="0 0 40 34"><path d="M20 33 4 17A9.5 9.5 0 0 1 20 5a9.5 9.5 0 0 1 16 12z" fill="#f07a2a"/></svg></div>
  <div class="service__name">NETWORK SECURITY</div>
  <div class="service__text">Lorem ipsum dolor sit amet,<br>consectetur adipisicing elit</div>
</div>

<section class="about" role="img" aria-label="Darkened office photo background">
  <h2 class="about__title">flexible solutions for your business needs</h2>
  <p class="about__text">Velmarketa is a technology solution provider based in Larkmoor, Westvale. Our goal is to make technology a non-issue for individuals and small to medium size businesses ranging from 5 to 150 Users. Velmarketa has the experience, the tools, high-level technology solutions and training to power your business and your work force. We</p>
</section>
</body>
</html>
```